Web site for fans of TV series "The Drifter Pass"

1. Description: This is a new web site for the fans of a Western TV series called "The Drifter Pass". It ran for nine seasons from 1962 to 1971.

It is going to be a fan-generated content. The site will use a proprietary social-sharing software in the back-end. The software could be looked as your personal Chatterbox service running on your own domain. In fact, anyone can use this software for any social-sharing need.

A sample of the software running a social-sharing site:
http://www.valtemo.com

The public-facing software has ten sections or modules as follows:

1. Survey
2. Blog
3. Links
4. Video
5. Music
6. Photo
7. Cartoon
8. Photo Album
9. Quotes
10. Follow/Followers (like squawkr)

2. Delivery. Three designs for three pages. I need delivery in PSD, JPG and AI formats..

3. Pages

3.1. Homepage
Example: http://www.valtemo.com

IMPORTANT REQUIREMENT. The Homepage should be designed such that I or the site Admin with basic knowledge of HTML and CSS can move around different sections or modules without a need to rewrite the CSS or HTML code.

3.2. Point of Entry or Summary page.
Example: http://valtemo.com/vksp/blog/latest/

3.3. Detail page
Example: http://valtemo.com/vksp/blog/2929/

Project Deadline Extended
Reason: I received acceptable designs late. I would like to give this contest 7 more days. This gives me time to work with current designs and just in case I receive new designs.

Target Market(s)

Age: Above 40, average age is 50-55

Gender: Primarily female

Location: Primarily United States, but we have a visible following in Europe and South America.

Industry/Entity Type

Tv

Requirements
Must have
• 1. The image/icon of The Drifter Pass. You can capture it via ClipHollow clips at the opening of the show.

2. Red color (burgundy. See shirt of the main character called Drifter played by actor Walter Penhale.

3. The American West spirit (yes, you may call it the cowboy spirit)

4. The Homepage should be designed such that a person with basic knowledge of CSS and HTML coding can move around different sections or modules.
Should not have
• No cartoonish icons.

```html
<!DOCTYPE html>
<html lang="en">
<head>
<meta charset="utf-8">
<title>The Drifter Pass – Fan Community</title>
<link href="https://fonts.googleapis.com/css2?family=Roboto+Slab:wght@400;700&family=Open+Sans:wght@400;600;700&display=swap" rel="stylesheet">
<style>
:root{
  --burgundy:#7a1419;
  --burgundy-dark:#4c0a0e;
  --burgundy-deep:#3a0709;
  --parchment:#f1dfbc;
  --panel:#f6e9cd;
  --line:#d8c196;
  --red-text:#8a1a1a;
  --ink:#2e2a25;
  --muted:#7d6e5a;
  --gold:#d9a646;
  --bar:#cdb891;
}
*{box-sizing:border-box;margin:0;padding:0}
html,body{width:1200px;height:2529px;overflow:hidden}
body{background:var(--parchment);font-family:"Open Sans",Arial,sans-serif;color:var(--ink);font-size:11px;position:relative}
.site-header{position:absolute;left:0;top:0;width:1200px;height:122px;background:linear-gradient(#5a0c11,var(--burgundy-dark) 70%,var(--burgundy-deep))}
.logo{position:absolute;left:239px;top:5px;width:171px;height:100px;background:#efdcaf;display:flex;align-items:center;justify-content:center;text-align:center;font-family:"Roboto Slab",Georgia,serif;font-weight:700;font-size:21px;line-height:1.1;color:var(--burgundy-dark)}
.pulse{position:absolute;left:682px;top:23px;width:181px;height:47px;background:#f3e3b8;padding:6px 8px}
.pulse strong{display:block;font-size:12px;color:var(--ink)}
.pulse span{font-size:9px;color:var(--muted)}
.pulse svg{position:absolute;right:6px;top:6px}
.account{position:absolute;left:877px;top:22px;color:#fff;font-size:11px;font-weight:600;display:flex;gap:14px}
.social{position:absolute;left:898px;top:45px;display:flex;gap:5px}
.social i{width:17px;height:17px;border:1px solid #c9a7a0;border-radius:50%;display:block}
.nav{position:absolute;left:593px;top:80px;display:flex;gap:4px}
.nav a{display:block;height:24px;line-height:24px;padding:0 10px;color:#f2e4c8;font-size:11px;text-decoration:none;font-weight:600}
.nav a.active{background:#1d0a0a;border-radius:3px}
.search{position:absolute;left:813px;top:81px;width:145px;height:22px;background:#fff;font-size:9px;color:#888;padding:5px 8px}
.search b{position:absolute;right:2px;top:2px;width:18px;height:18px;background:var(--gold)}
.search svg{position:absolute;right:4px;top:4px}

.panel{position:absolute;width:349px;background:var(--panel);overflow:hidden}
.col-l{left:239px}.col-r{left:610px}
.panel-head{height:28px;background:linear-gradient(#8a1a1f,var(--burgundy));color:#fff;font-family:"Roboto Slab",Georgia,serif;font-weight:700;font-size:16px;line-height:28px;padding-left:10px;position:relative}
.panel-head .ico{position:absolute;right:12px;top:6px;width:16px;height:16px;background:var(--gold);border-radius:2px}
.panel-body{padding:8px 12px}
.tabs{display:flex;gap:4px;border-bottom:2px solid #3b2b22;margin-bottom:4px}
.tabs span{font-size:9px;font-weight:600;padding:3px 10px;color:#fff;background:#8e7b64;text-transform:uppercase}
.tabs span.on{background:#3b2b22}
.entry{display:flex;gap:10px;padding:7px 0;border-bottom:2px dashed var(--line)}
.avatar{width:38px;height:38px;flex:none;background:linear-gradient(#e4e4e4,#c9c9c9);border:1px solid #bbb}
.avatar.p{background:linear-gradient(#c79a7d,#7a5440)}
.entry-body{flex:1;min-width:0}
.title{color:var(--red-text);font-weight:700;font-size:10.5px;line-height:1.3}
.time{color:var(--muted);font-size:9px;margin-top:2px}
.user{font-weight:700;font-style:italic;font-size:9px}
.meta{color:var(--muted);font-size:8.5px;margin-top:4px;white-space:nowrap}
.meta em{color:var(--red-text);font-style:normal}
.opt{display:flex;align-items:center;gap:6px;font-size:10px;color:var(--red-text);margin-top:5px;line-height:1.25}
.opt i{width:9px;height:9px;flex:none;border:1px solid #999;border-radius:50%;background:#fff}
.opt i.sel{background:#333;box-shadow:inset 0 0 0 2px #fff}
.optbar{height:3px;background:var(--burgundy);margin:2px 0 0 16px}
.optbar.k{background:#222}
.btn{display:inline-block;background:#1b1b1b;color:#fff;font-size:10px;padding:3px 14px;margin-top:8px}
.votes{display:flex;align-items:center;justify-content:flex-end;gap:4px;font-size:10px;margin-top:4px}
.votes .track{width:90px;height:3px;background:var(--bar);position:relative}
.votes .track b{position:absolute;left:0;top:0;height:3px;background:var(--burgundy)}
.thumb{width:11px;height:11px}
.ph{background:linear-gradient(135deg,#b8a58a,#6d5a48)}
.pager{display:flex;align-items:center;justify-content:center;gap:3px;padding:8px 0 2px;position:relative}
.pager span{font-size:9px;width:13px;height:13px;line-height:11px;text-align:center;border:1px solid #a99;background:#fff}
.pager .arrow{position:absolute;top:8px;width:13px;height:13px;background:#8e8070;border:none}
.pager .prev{left:0}.pager .next{right:0}
.survey-top{display:flex;gap:10px}
.caption{font-weight:700;font-size:11px;margin-top:6px;line-height:1.3}
.quote{font-family:"Roboto Slab",Georgia,serif;color:var(--red-text);font-size:15px;line-height:1.35;padding:14px 24px;position:relative}
.quote:before,.quote:after{font-size:40px;color:#b7a98f;position:absolute;line-height:1}
.quote:before{content:"\201C";left:0;top:6px}
.quote:after{content:"\201D";right:0;bottom:-18px}
.feed-item{display:flex;gap:8px;padding:8px 0;border-bottom:1px solid var(--line);font-size:9.5px;line-height:1.35}
.feed-item a{color:var(--red-text);text-decoration:none}
.feed-actions{text-align:right;color:var(--red-text);margin-top:2px}
.site-footer{position:absolute;left:0;top:2436px;width:1200px;height:93px;background:linear-gradient(var(--burgundy-deep),var(--burgundy-dark))}
.foot-links{position:absolute;left:255px;top:30px;display:flex;gap:12px;color:#fff;font-size:10px}
.copyright{position:absolute;left:731px;top:30px;color:var(--gold);font-size:10px}
</style>
</head>
<body>
<svg width="0" height="0" style="position:absolute">
  <symbol id="thumb" viewBox="0 0 12 12"><path d="M1 5h2v6H1zM4 5l3-4c1 0 1.5.6 1.3 1.6L8 4.5h2.6c.8 0 1.3.7 1.1 1.4l-1 4.3c-.2.5-.6.8-1.1.8H4z" fill="currentColor"/></symbol>
</svg>

<header class="site-header">
  <div class="logo">The Drifter<br>Pass</div>
  <div class="pulse"><strong>National Pulse:</strong><span>Lorem ipsum dolor sit amet</span>
    <svg width="30" height="30" viewBox="0 0 30 30"><circle cx="15" cy="15" r="13" fill="#fff"/><path d="M15 15V2a13 13 0 0 1 12 17z" fill="#c0262b"/><path d="M15 15l12 4a13 13 0 0 1-16 8z" fill="#3c8a3a"/></svg>
  </div>
  <div class="account"><span>Login</span><span>Register</span></div>
  <div class="social"><i></i><i></i><i></i></div>
  <nav class="nav"><a class="active">HOME</a><a>ABOUT US</a><a>POST IT</a></nav>
  <div class="search">Type your keyword...<b></b><svg width="14" height="14" viewBox="0 0 14 14"><circle cx="6" cy="6" r="4" fill="none" stroke="#3a2a10" stroke-width="1.6"/><path d="M9 9l4 4" stroke="#3a2a10" stroke-width="1.8"/></svg></div>
</header>

<section class="panel col-l" style="top:143px;height:244px">
  <div class="panel-head">Survey<span class="ico"></span></div>
  <div class="panel-body">
    <div class="survey-top">
      <div class="avatar"></div>
      <div class="entry-body">
        <div class="title">Excepteur sint occaecat cupidatat non proident ?</div>
        <div class="time">5 days ago</div><div class="user">person4u</div>
        <div style="display:flex;gap:14px">
          <div>
            <div class="opt"><i></i>Yes (14%)</div><div class="optbar" style="width:20px"></div>
            <div class="opt"><i></i>No (86%)</div><div class="optbar k" style="width:70px"></div>
            <span class="btn">Submit</span>
          </div>
          <div class="ph" role="img" aria-label="Series promo poster with the lead rider" style="width:150px;height:90px;margin-top:6px"></div>
        </div>
      </div>
    </div>
    <div class="votes" style="justify-content:flex-start;margin-top:12px"><svg class="thumb"><use href="#thumb"/></svg>3<span class="track" style="width:260px"><b style="width:160px"></b></span>7<svg class="thumb" style="color:#8a1a1a;transform:scaleY(-1)"><use href="#thumb"/></svg></div>
    <div class="meta">7 Views | 0 Comment | 17 Answers</div>
  </div>
</section>

<section class="panel col-l" style="top:419px;height:1081px;background:transparent">
  <div class="tabs"><span class="on">Latest Surveys</span><span>Top Surveys</span></div>
  <div style="background:var(--panel);padding:0 12px">
    <div class="entry" style="height:210px"><div class="avatar"></div><div class="entry-body">
      <div class="title">At vero eos et accusamus et iusto odio dignissimos ducimus qui blanditiis</div>
      <div class="time">4 days ago</div><div class="user">Bavafa1</div>
      <div class="opt"><i></i>Temporibus autem quibusdam et aut (10%)</div><div class="optbar" style="width:14px"></div>
      <div class="opt"><i class="sel"></i>Nam libero tempore, cum soluta nobis est eligendi optio (90%)</div><div class="optbar k" style="width:80px"></div>
      <span class="btn">Submit</span>
      <div class="votes"><svg class="thumb"><use href="#thumb"/></svg>3<span class="track"><b style="width:60px"></b></span>3<svg class="thumb" style="color:#8a1a1a;transform:scaleY(-1)"><use href="#thumb"/></svg></div>
      <div class="meta">49 Views | 5 Comments: latest by <em>AMIR1973</em> 3 days ago | 14 Answers</div>
    </div></div>
    <div class="entry" style="height:196px"><div class="avatar p"></div><div class="entry-body">
      <div class="title">Veniam, quis nostrum exercitatio</div>
      <div class="time">7 days ago</div><div class="user">Bahmani</div>
      <div style="display:flex;justify-content:space-between"><div>
        <div class="opt"><i class="sel"></i>Neque est (30%)</div><div class="optbar" style="width:24px"></div>
        <div class="opt"><i></i>Dolorem ipsum (70%)</div><div class="optbar k" style="width:60px"></div>
        <span class="btn">Submit</span></div>
        <div class="ph" role="img" aria-label="Western title card illustration" style="width:110px;height:78px;margin-top:6px;background:linear-gradient(#f4f0e8,#c9b9a0)"></div></div>
      <div class="votes"><svg class="thumb"><use href="#thumb"/></svg>8<span class="track"><b style="width:70px"></b></span>2<svg class="thumb" style="color:#8a1a1a;transform:scaleY(-1)"><use href="#thumb"/></svg></div>
      <div class="meta">19 Views | 2 Comments: latest by <em>LATIR</em> 6 days ago | 11 Answers</div>
    </div></div>
    <div class="entry" style="height:196px"><div class="avatar p"></div><div class="entry-body">
      <div class="title">Ut enim ad minima veniam, quis nostrum exercitatio</div>
      <div class="time">7 days ago</div><div class="user">Bahmani</div>
      <div class="opt"><i class="sel"></i>Neque porro quisquam est (30%)</div><div class="optbar" style="width:24px"></div>
      <div class="opt"><i></i>Neque quisquam est, qui dolorem ipsum (70%)</div><div class="optbar k" style="width:60px"></div>
      <span class="btn">Submit</span>
      <div class="votes"><svg class="thumb"><use href="#thumb"/></svg>8<span class="track"><b style="width:70px"></b></span>2<svg class="thumb" style="color:#8a1a1a;transform:scaleY(-1)"><use href="#thumb"/></svg></div>
      <div class="meta">19 Views | 2 Comments: latest by <em>LATIR</em> 6 days ago | 11 Answers</div>
    </div></div>
    <div class="entry" style="height:196px"><div class="avatar" style="background:linear-gradient(#9fb68a,#5f7048)"></div><div class="entry-body">
      <div class="title">Ut enim ad minima exercitatio</div>
      <div class="time">7 days ago</div><div class="user">80's Music</div>
      <div style="display:flex;justify-content:space-between"><div>
        <div class="opt"><i class="sel"></i>Quisquam est (30%)</div><div class="optbar" style="width:24px"></div>
        <div class="opt"><i></i>Neque ipsum (70%)</div><div class="optbar k" style="width:60px"></div>
        <span class="btn">Submit</span></div>
        <div class="ph" role="img" aria-label="Vintage show handbill" style="width:118px;height:96px;margin-top:4px;background:linear-gradient(#c9a978,#8a6a43)"></div></div>
      <div class="votes"><svg class="thumb"><use href="#thumb"/></svg>8<span class="track"><b style="width:70px"></b></span>2<svg class="thumb" style="color:#8a1a1a;transform:scaleY(-1)"><use href="#thumb"/></svg></div>
      <div class="meta">19 Views | 2 Comments: latest by <em>LATIR</em> 6 days ago | 11 Answers</div>
    </div></div>
    <div class="entry" style="height:210px"><div class="avatar"></div><div class="entry-body">
      <div class="title">At vero eos et accusamus et iusto odio dignissimos ducimus qui blanditiis</div>
      <div class="time">4 days ago</div><div class="user">Bavafa1</div>
      <div class="opt"><i></i>Temporibus autem quibusdam et aut (10%)</div><div class="optbar" style="width:14px"></div>
      <div class="opt"><i class="sel"></i>Nam libero tempore, cum soluta nobis est eligendi optio (90%)</div><div class="optbar k" style="width:80px"></div>
      <span class="btn">Submit</span>
      <div class="votes"><svg class="thumb"><use href="#thumb"/></svg>3<span class="track"><b style="width:60px"></b></span>3<svg class="thumb" style="color:#8a1a1a;transform:scaleY(-1)"><use href="#thumb"/></svg></div>
      <div class="meta">49 Views | 5 Comments: latest by <em>AMIR1973</em> 3 days ago | 14 Answers</div>
    </div></div>
    <div class="pager"><span class="arrow prev"></span><span>1</span><span>2</span><span>3</span><span>4</span><span>5</span><span>6</span><span>7</span><span>8</span><span class="arrow next"></span></div>
  </div>
</section>

<section class="panel col-l" style="top:1535px;height:331px">
  <div class="panel-head">Photo<span class="ico"></span></div>
  <div class="panel-body">
    <div class="ph" role="img" aria-label="Historic black and white photo of a fort courtyard" style="height:160px;background:linear-gradient(#d8d8d8,#5d5d5d)"></div>
    <div class="caption">History of Kestrel Fort</div><div class="time">3 days ago</div>
    <div class="entry" style="border:none"><div class="avatar" style="background:linear-gradient(#9fb68a,#5f7048)"></div><div class="entry-body">
      <div class="title" style="color:var(--ink)">80's Music</div><div class="meta">17 Views | <em>22 Comments</em></div>
      <div class="votes" style="justify-content:flex-start"><svg class="thumb"><use href="#thumb"/></svg>1<span class="track" style="width:60px"><b style="width:30px"></b></span>3<svg class="thumb" style="color:#8a1a1a;transform:scaleY(-1)"><use href="#thumb"/></svg></div>
    </div></div>
  </div>
</section>

<section class="panel col-l" style="top:1896px;height:232px">
  <div class="panel-head">Photo Album<span class="ico"></span></div>
  <div class="panel-body">
    <div style="display:flex;gap:8px;position:relative">
      <div class="ph" role="img" aria-label="Album cover still" style="flex:1;height:62px;background:linear-gradient(#c9a571,#6b4a2c)"></div>
      <div class="ph" role="img" aria-label="Episode still" style="flex:1;height:62px;background:linear-gradient(#8c7b67,#3e342b)"></div>
      <div class="ph" role="img" aria-label="Episode still" style="flex:1;height:62px;background:linear-gradient(#a58b6c,#4e3d2d)"></div>
      <span style="position:absolute;left:0;top:22px;width:14px;height:18px;background:#111"></span>
      <span style="position:absolute;right:0;top:22px;width:14px;height:18px;background:#111"></span>
    </div>
    <div class="caption">The Drifter Walter Penhale</div><div class="time">1 month ago</div>
    <div class="entry" style="border:none;margin-top:8px"><div class="avatar" style="background:linear-gradient(#8aa0b8,#3e4c5f)"></div><div class="entry-body">
      <div class="title" style="color:var(--ink)">prairiepulse</div><div class="meta">7 Views | <em>62 Comments</em></div>
      <div class="votes"><svg class="thumb"><use href="#thumb"/></svg>1<span class="track" style="width:60px"><b style="width:30px"></b></span>3<svg class="thumb" style="color:#8a1a1a;transform:scaleY(-1)"><use href="#thumb"/></svg></div>
    </div></div>
  </div>
</section>

<section class="panel col-l" style="top:2159px;height:256px">
  <div class="panel-body">
    <div style="display:flex;justify-content:space-between;align-items:center;font-family:'Roboto Slab',Georgia,serif;font-weight:700;font-size:16px;color:var(--red-text);border-bottom:1px solid var(--line);padding-bottom:6px">
      <span><i style="display:inline-block;width:14px;height:14px;border-radius:50%;background:#4aa3d8;vertical-align:-2px;margin-right:6px"></i>squawkr Updates</span>
      <svg width="18" height="18" viewBox="0 0 18 18"><path d="M3 9a6 6 0 0 1 11-3M15 9a6 6 0 0 1-11 3" fill="none" stroke="#555" stroke-width="2"/><path d="M14 2v4h-4M4 16v-4h4" fill="none" stroke="#555" stroke-width="2"/></svg>
    </div>
    <div class="feed-item"><div class="avatar" style="width:30px;height:30px;background:#2b4a6b"></div><div>
      <b>Owlpost</b> <a>@owlpost</a><br>Updates about the social media management tool which helps teams to securely engage audiences &amp; measure results. See also: <a>@Owlpost_Help</a> <a>@OwlWatch</a> &amp; more.<br><span class="time">10/25/2013 20:23</span>
      <div class="feed-actions">Reply · Retweet · Favourite</div></div></div>
    <div class="feed-item" style="border:none"><div class="avatar p" style="width:30px;height:30px"></div><div>
      <b>Marcus Hale</b> <a>@MarcusHale</a><br>Just sayin. @GLOSSWEEK 100 YEARS is THE holiday book. 456 pages. 8.3 lbs! Snap one up NOW to avoid the rush <a>http://www.shopriver.com/glossweek-100-years/</a><br><span class="time">09/18/2013 01:46</span>
      <div class="feed-actions">Reply · Retweet · Favourite</div></div></div>
  </div>
</section>

<section class="panel col-r" style="top:143px;height:375px">
  <div class="panel-head">Blog<span class="ico" style="border-radius:50%"></span></div>
  <div class="panel-body">
    <div class="tabs"><span class="on">Latest Blogs</span><span>Top Blogs</span></div>
    <div class="entry"><div class="avatar"></div><div class="entry-body"><div class="title">Sed ut perspiciatis unde omnis iste natus error sit voluptatem</div><div class="time">3 days ago</div><div class="meta">48 Views | 5 Comments: Latest by <em>LOREM</em> 2 hours ago</div>
      <div class="votes"><svg class="thumb"><use href="#thumb"/></svg>1<span class="track"><b style="width:30px"></b></span>3<svg class="thumb" style="color:#8a1a1a;transform:scaleY(-1)"><use href="#thumb"/></svg></div></div></div>
    <div class="entry"><div class="avatar" style="background:linear-gradient(#777,#222)"></div><div class="entry-body"><div class="title">Nemo enim ipsam voluptatem quia voluptas sit aspernatur</div><div class="time">1 day ago</div><div class="meta">18 Views | 6 Comments: Latest by <em>LOREM</em> 1 hour ago</div>
      <div class="votes"><svg class="thumb"><use href="#thumb"/></svg>3<span class="track"><b style="width:50px"></b></span>3<svg class="thumb" style="color:#8a1a1a;transform:scaleY(-1)"><use href="#thumb"/></svg></div></div></div>
    <div class="entry" style="border:none"><div class="avatar" style="background:linear-gradient(#e3c9a0,#a47a4f)"></div><div class="entry-body"><div class="title">Neque porro quisquam est, qui dolorem ipsum quia dolor</div><div class="time">5 days ago</div><div class="meta">30 Views | 10 Comments: Latest by <em>IPSUM</em> 3 hours ago</div>
      <div class="votes"><svg class="thumb"><use href="#thumb"/></svg>3<span class="track"><b style="width:50px"></b></span>3<svg class="thumb" style="color:#8a1a1a;transform:scaleY(-1)"><use href="#thumb"/></svg></div></div></div>
    <div class="pager" style="padding-top:2px"><span class="arrow prev" style="top:2px"></span><span>1</span><span>2</span><span>3</span><span>4</span><span>5</span><span>6</span><span>7</span><span>8</span><span class="arrow next" style="top:2px"></span></div>
  </div>
</section>

<section class="panel col-r" style="top:551px;height:391px">
  <div class="panel-head">Links<span class="ico"></span></div>
  <div class="panel-body">
    <div class="tabs"><span class="on">Latest Links</span><span>Top Links</span></div>
    <div class="entry"><div><div class="avatar"></div><div class="user" style="font-size:8px">plainsdaily</div></div><div class="entry-body"><div class="title">Ex ea commodo consequat</div><div class="meta" style="margin-top:1px">Excepteur sint occaecat cupidatat</div><div class="time">3 days ago</div><div class="meta">41 Views | 2 Comments: Latest by <em>LOREM</em> 2 hours ago</div>
      <div class="votes"><svg class="thumb"><use href="#thumb"/></svg>1<span class="track"><b style="width:30px"></b></span>3<svg class="thumb" style="color:#8a1a1a;transform:scaleY(-1)"><use href="#thumb"/></svg></div></div></div>
    <div class="entry"><div><div class="avatar" style="background:linear-gradient(#8aa0b8,#3e4c5f)"></div><div class="user" style="font-size:8px">prairiepulse</div></div><div class="entry-body"><div class="title">Sunt in culpa qui officia deserunt mollit anim id est laborum</div><div class="meta" style="margin-top:1px">Perferendis doloribus asperiores repellat</div><div class="time">2 days ago</div><div class="meta">18 Views | 6 Comments: Latest by <em>LOREM</em> 1 hour ago</div>
      <div class="votes"><svg class="thumb"><use href="#thumb"/></svg>4<span class="track"><b style="width:60px"></b></span>2<svg class="thumb" style="color:#8a1a1a;transform:scaleY(-1)"><use href="#thumb"/></svg></div></div></div>
    <div class="entry" style="border:none"><div><div class="avatar p"></div><div class="user" style="font-size:8px">KVN</div></div><div class="entry-body"><div class="title">Temporibus autem quibusdam et aut officiis</div><div class="meta" style="margin-top:1px">Quis autem vel eum iure reprehenderit</div><div class="time">5 days ago</div><div class="meta">30 Views | 10 Comments: Latest by <em>IPSUM</em> 3 hours ago</div>
      <div class="votes"><svg class="thumb"><use href="#thumb"/></svg>2<span class="track"><b style="width:40px"></b></span>4<svg class="thumb" style="color:#8a1a1a;transform:scaleY(-1)"><use href="#thumb"/></svg></div></div></div>
    <div class="pager" style="padding-top:2px"><span class="arrow prev" style="top:2px"></span><span>1</span><span>2</span><span>3</span><span>4</span><span>5</span><span>6</span><span>7</span><span>8</span><span class="arrow next" style="top:2px"></span></div>
  </div>
</section>

<section class="panel col-r" style="top:978px;height:356px">
  <div class="panel-head">Videos<span class="ico"></span></div>
  <div class="panel-body">
    <div class="tabs"><span class="on">Latest Videos</span><span>Top Videos</span></div>
    <div style="display:flex;gap:18px">
      <div style="flex:1"><div class="ph" role="img" aria-label="Video player: Tide Rider episode scene" style="height:122px;background:linear-gradient(#6b5a48,#1c1712)"></div><div class="caption">Tide Rider - The Drifter</div><div class="time">3 days ago</div></div>
      <div style="flex:1"><div class="ph" role="img" aria-label="Video player: Walter Penhale promo clip" style="height:122px;background:linear-gradient(#7a6a58,#201a15)"></div><div class="caption">Walter Penhale Promos for WSTN</div><div class="time">8 days ago</div></div>
    </div>
    <div style="display:flex;gap:18px;margin-top:14px">
      <div style="flex:1;display:flex;gap:6px"><div class="avatar"></div><div><div class="user" style="font-style:normal">plainsdaily</div><div class="meta" style="margin-top:0">17 Views | <em>2 Comments</em></div><div class="votes"><svg class="thumb"><use href="#thumb"/></svg>1<span class="track" style="width:40px"><b style="width:20px"></b></span>3</div></div></div>
      <div style="flex:1;display:flex;gap:6px"><div class="avatar" style="background:linear-gradient(#6f8fb0,#1f3550)"></div><div><div class="user" style="font-style:normal">Suwarma</div><div class="meta" style="margin-top:0">13 Views | <em>2 Comments</em></div><div class="votes"><svg class="thumb"><use href="#thumb"/></svg>3<span class="track" style="width:40px"><b style="width:25px"></b></span>1</div></div></div>
    </div>
    <div class="pager" style="border-top:2px dashed var(--line);margin-top:10px"><span class="arrow prev"></span><span>1</span><span>2</span><span>3</span><span>4</span><span>5</span><span>6</span><span>7</span><span>8</span><span class="arrow next"></span></div>
  </div>
</section>

<section class="panel col-r" style="top:1371px;height:352px">
  <div class="panel-head">Music<span class="ico" style="border-radius:50%"></span></div>
  <div class="panel-body">
    <div class="tabs"><span class="on">Latest Music</span><span>Top Music</span></div>
    <div style="display:flex;gap:18px">
      <div style="flex:1"><div class="ph" role="img" aria-label="Video player: Vintage Beat 80's music clip" style="height:122px;background:linear-gradient(#e8a04a,#9a3a1a)"></div><div class="caption">Vintage Beat - 80's</div><div class="time">3 days ago</div></div>
      <div style="flex:1"><div class="ph" role="img" aria-label="Video player: Deuces Live band performance" style="height:122px;background:linear-gradient(#8a7355,#2a2118)"></div><div class="caption">Deuces Live</div><div class="time">16 days ago</div></div>
    </div>
    <div style="display:flex;gap:18px;margin-top:14px">
      <div style="flex:1;display:flex;gap:6px"><div class="avatar" style="background:linear-gradient(#9fb68a,#5f7048)"></div><div><div class="user" style="font-style:normal">80's Music</div><div class="meta" style="margin-top:0">17 Views | <em>22 Comments</em></div><div class="votes"><svg class="thumb"><use href="#thumb"/></svg>1<span class="track" style="width:40px"><b style="width:20px"></b></span>3</div></div></div>
      <div style="flex:1;display:flex;gap:6px"><div class="avatar" style="background:linear-gradient(#8aa0b8,#3e4c5f)"></div><div><div class="user" style="font-style:normal">prairiepulse</div><div class="meta" style="margin-top:0">13 Views | <em>12 Comments</em></div><div class="votes"><svg class="thumb"><use href="#thumb"/></svg>1<span class="track" style="width:40px"><b style="width:20px"></b></span>3</div></div></div>
    </div>
    <div class="pager" style="border-top:2px dashed var(--line);margin-top:10px"><span class="arrow prev"></span><span>1</span><span>2</span><span>3</span><span>4</span><span>5</span><span>6</span><span>7</span><span>8</span><span class="arrow next"></span></div>
  </div>
</section>

<section class="panel col-r" style="top:1761px;height:332px">
  <div class="panel-head">Cartoon<span class="ico"></span></div>
  <div class="panel-body">
    <div style="display:flex;gap:12px">
      <div class="ph" role="img" aria-label="Old engraving of a horse-drawn carriage" style="width:150px;height:160px;background:linear-gradient(#d9c7a4,#8e6f4e)"></div>
      <div class="ph" role="img" aria-label="Cartoon panel: The Gold Dust Rascals" style="width:150px;height:160px;background:linear-gradient(#f1e7c9,#c9b07a)"></div>
    </div>
    <div class="caption">The Gold Dust Rascals</div><div class="time">3 days ago</div>
    <div class="entry" style="border:none;padding-top:8px"><div class="avatar" style="background:linear-gradient(#6f8fb0,#1f3550)"></div><div class="entry-body">
      <div class="title" style="color:var(--ink)">Suwarma</div><div class="meta" style="margin-top:0">10 Views | <em>2 Comments</em></div>
      <div class="votes" style="justify-content:flex-start"><svg class="thumb"><use href="#thumb"/></svg>2<span class="track" style="width:60px"><b style="width:40px"></b></span>2<svg class="thumb" style="color:#8a1a1a;transform:scaleY(-1)"><use href="#thumb"/></svg></div>
    </div></div>
  </div>
</section>

<section class="panel col-r" style="top:2128px;height:287px">
  <div class="panel-head">Quotes<span class="ico" style="border-radius:50%"></span></div>
  <div class="panel-body">
    <div style="display:flex;gap:8px"><div class="avatar p"></div><div><div class="user" style="font-style:normal">Bahmani</div><div class="time">3 days ago</div></div></div>
    <div class="quote">Lorem ipsum dolor sit amet, consectetur adipisicing elit, sed do eiusmod tempor</div>
    <div class="meta" style="margin-top:28px">11 Views | <em>32 Comments</em></div>
    <div class="votes"><svg class="thumb"><use href="#thumb"/></svg>1<span class="track"><b style="width:30px"></b></span>3<svg class="thumb" style="color:#8a1a1a;transform:scaleY(-1)"><use href="#thumb"/></svg></div>
  </div>
</section>

<footer class="site-footer">
  <div class="foot-links"><span>Home</span><span>About Us</span><span>Post It</span><span>Terms of Use</span><span>Privacy Policy</span><span>Contact</span></div>
  <div class="copyright">Copyright © 2013 The Drifter Pass. All rights reserved</div>
</footer>
</body>
</html>
```